Präsentationsvorlagen für Anbieter von innovativen Softwarelösungen
Zielgruppe
quamvel ist ein internationales Unternehmen, das individuelle, zukunftssichere und innovative Softwarelösungen anbietet. Mit Lantrava machen wir unsere Kunden zum Dirigenten ihrer Daten, indem wir interne und externe IT-Systeme und Dienste flexibel, sicher und zuverlässig miteinander verbinden. Kunden aus verschiedenen Branchen wie der Fertigungsindustrie und der allgemeinen Wirtschaft vertrauen bei der Umsetzung innovativer Integrationsprojekte auf unsere Lösung. Mit Plug & Produce durch unseren Lantrava Industrial Service Bus und dem Einsatz internationaler Standards wie OPC UA und MQTT ermöglichen wir unseren Kunden, zukunftsorientierte Projekte erfolgreich und nachhaltig umzusetzen.
Aufgabenstellung
Wir benötigen neue Präsentationsvorlagen für Powerpoint:
Unsere alten Masterfoliensätze in Powerpoint und Printmedien (Whitepaper, Success Stories) wirken noch ziemlich altbacken und nicht modern. Die Website wurde erst gegen Anfang Mai komplett neu released und entspricht nun größtenteils der Darstellung wie wir auftreten möchten. Unsere Farben (siehe Style Guide) sind größtenteils Blautöne, die wir aber gerne mit einem Lime-Grün als Akzentfarbe für den Kontrast auflockern, ansonsten arbeiten wir viel mit Weißflächen.
Wir würden uns moderne und cleane Design-Entwürfe für die Powerpoint-Präsentation wünschen (am besten direkt als Masterfoliensatz in PPT), die gut zu den Infografiken, wie man sie vor allem oftmals auf der Website sieht, passen. Die Präsentationen sollten im üblichen 16:9-Format angelegt sein.

```html
<!DOCTYPE html>
<html lang="de">
<head>
<meta charset="utf-8">
<title>Lantrava – Präsentationsvorlage</title>
<link href="https://fonts.googleapis.com/css2?family=Open+Sans:wght@400;600;700;800&family=Nunito:wght@800;900&display=swap" rel="stylesheet">
<style>
:root{
  --blue-deep:#0d3f78;
  --blue:#14609f;
  --blue-mid:#1b7cc4;
  --sky:#1ea3e2;
  --lime:#b9d84a;
  --lime-soft:#d7ea8f;
  --pale:#e4f2fb;
  --ink:#1d2b3a;
  --grey:#7d8895;
  --grey-soft:#a9b2bc;
  --canvas:#e2e3e4;
  --white:#fff;
}
*{box-sizing:border-box;margin:0;padding:0}
html,body{width:1200px;height:3592px;overflow:hidden}
body{background:var(--canvas);font-family:"Open Sans",Arial,sans-serif;color:var(--ink);position:relative}
.stage-top{position:absolute;left:0;top:0;width:1200px;height:580px;background:linear-gradient(135deg,#f4f9fd,#dcecf7)}
.mini{position:absolute;transform-origin:0 0;transform:scale(.68)}
.slide{position:absolute;width:520px;height:293px;overflow:hidden;background:linear-gradient(130deg,#fff 35%,#e2f0fa 100%);box-shadow:0 2px 6px rgba(0,0,0,.08)}
.abs{position:absolute}
.brand{position:absolute;display:flex;align-items:center;gap:4px;font-size:10px;color:var(--grey)}
.brand i{display:block;width:8px;height:8px;border-radius:50%;border:1.5px solid var(--blue-mid)}
.brand.light{color:#fff}.brand.light i{border-color:#fff}
.brand.r{top:16px;right:16px}
.hd{position:absolute;left:24px;top:14px}
.hd .bar{position:absolute;left:-24px;top:0;width:5px;height:24px;background:var(--sky)}
.hd h2{font-size:12px;font-weight:700;letter-spacing:.2px}
.hd p{font-size:7px;color:var(--blue-mid)}
.foot{position:absolute;left:20px;bottom:10px;font-size:4.5px;color:var(--grey)}
.pg{position:absolute;right:8px;bottom:8px;width:14px;height:10px;background:var(--lime)}
.photo{position:absolute;border-radius:50%;background:radial-gradient(circle at 40% 40%,#8aa3b8,#3d5870 70%,#2a3f55)}
.ring{position:absolute;border-radius:50%;background:linear-gradient(160deg,var(--sky),var(--blue))}
.lead{font-size:7px;font-weight:700;color:var(--blue)}
.body{font-size:5px;color:#4a5562;line-height:1.45}
.body li{margin-left:9px}
.body li li{margin-left:12px}
.pill{position:absolute;border-radius:8px;font-size:5px;display:flex;align-items:center;justify-content:center}
.agenda-row{position:absolute;left:174px;width:292px;display:flex;align-items:center;font-size:6.5px;font-weight:700}
.agenda-row span.line{flex:1;border-bottom:1px dotted var(--grey-soft);margin:0 6px}
.agenda-row::before{content:"";width:4px;height:4px;border-radius:50%;background:var(--lime);margin-right:6px;margin-left:-10px}
.subitem{position:absolute;font-size:6.5px;font-weight:700;color:var(--blue)}
.subitem small{display:block;font-size:5px;font-weight:400;color:var(--grey);margin-left:8px}
.card{position:absolute;top:78px;width:140px;height:160px;background:#fff;box-shadow:0 1px 4px rgba(0,0,0,.1);text-align:center;padding:0 12px}
.card .ic{width:34px;height:34px;border-radius:50%;background:var(--blue-mid);margin:-10px auto 8px;border:4px solid #cfe6f5}
.card h3{font-size:7px;color:var(--blue);margin-bottom:10px}
.card .body{text-align:left}
table{border-collapse:collapse;width:100%;font-size:4.6px}
.num td{padding:2.6px 3px;border-bottom:1px solid #dfe6ec;text-align:right}
.num td:first-child{font-weight:700;width:100px}
.num th{background:var(--blue-deep);color:#fff;padding:3px;font-weight:600}
.num tr.hl td{background:#d9ecd0;padding:1.5px}
.txt th{color:#fff;padding:3px;font-size:5.5px}
.txt td{padding:6px 4px;vertical-align:top;color:#4a5562;border-bottom:1px solid #e5ebf0}
.txt td:first-child{color:var(--blue);font-weight:700;width:46px}
.member{position:absolute;top:80px;width:96px;text-align:center}
.member .ph{width:80px;height:80px;border-radius:50%;margin:0 auto 8px;background:#fff;border:2px solid #dbe9f4;box-shadow:0 1px 4px rgba(0,0,0,.08)}
.member h4{font-size:6px}
.member p{font-size:4.6px;color:var(--grey);margin:2px 0 4px}
.member .soc{display:flex;gap:2px;justify-content:center}
.member .soc i{width:6px;height:6px;background:var(--ink)}
.stat{position:absolute;top:204px;width:92px;height:48px;display:flex;align-items:center;gap:5px;padding:0 8px;color:#fff}
.stat b{font-size:14px;font-weight:800;display:block;line-height:1}
.stat small{font-size:4.5px;display:block}
</style>
</head>
<body>

<div class="stage-top">
  <div class="slide mini" style="left:33px;top:190px">
    <div class="brand" style="top:16px;left:20px"><i></i>Lantrava</div>
    <div class="ring" style="left:310px;top:52px;width:200px;height:200px"></div>
    <div class="photo" role="img" aria-label="Foto: Team bei einer Besprechung" style="left:300px;top:42px;width:190px;height:190px"></div>
    <h1 class="abs" style="left:36px;top:118px;font-size:16px;font-weight:800">Lantrava Industrial Suite</h1>
    <p class="abs" style="left:36px;top:142px;font-size:6px;color:var(--grey)">Wir machen Sie zum Dirigenten Ihrer Daten!</p>
    <div class="pill" style="left:36px;top:158px;width:56px;height:12px;background:var(--lime);color:#fff">Sep. 2023</div>
    <div class="brand" style="left:24px;bottom:20px;font-size:13px;color:var(--blue)"><i></i>quamvel</div>
  </div>
  <div class="slide mini" style="left:423px;top:190px">
    <div class="brand" style="top:16px;left:16px"><i></i>Lantrava</div>
    <div class="abs" style="left:0;top:66px;width:520px;height:160px;background:linear-gradient(120deg,var(--blue-mid),var(--blue))"></div>
    <div class="abs" style="left:104px;top:118px;font-size:34px;font-weight:300;color:transparent;-webkit-text-stroke:1px rgba(255,255,255,.55)">01</div>
    <div class="abs" style="left:176px;top:108px;color:#fff;font-size:13px;font-weight:700;line-height:1.15">Kapiteltrenner auch<br>zweizeilig möglich</div>
    <div class="abs" style="left:176px;top:146px;color:#fff;font-size:7px">Subheadline</div>
    <div class="pill" style="left:176px;top:170px;width:44px;height:11px;border:1px solid var(--lime);color:var(--lime)">Read more</div>
  </div>
  <div class="slide mini" style="left:813px;top:190px">
    <div class="hd"><span class="bar"></span><h2>HEADLINE</h2><p>Subheadline</p></div>
    <div class="brand r"><i></i>Lantrava</div>
    <div class="abs" role="img" aria-label="Weltkarte" style="left:130px;top:40px;width:360px;height:160px;background:linear-gradient(180deg,#c9ced4,#b3bac2);border-radius:40px"></div>
    <div class="abs" style="left:28px;top:196px;font-size:15px;font-weight:700">World Maps</div>
    <div class="stat" style="left:184px;background:var(--blue-deep)"><b>80%</b></div>
    <div class="stat" style="left:286px;background:var(--sky)"><b>85%</b></div>
    <div class="stat" style="left:388px;background:var(--lime)"><b>75%</b></div>
  </div>
</div>

<!-- 1 cover -->
<section class="slide" style="left:64px;top:654px">
  <div class="brand" style="top:16px;left:20px"><i></i>Lantrava</div>
  <div class="abs" style="top:18px;right:26px;font-size:5px;color:var(--grey)">www.ihredomain.de</div>
  <div class="ring" style="left:310px;top:52px;width:200px;height:200px"></div>
  <div class="photo" role="img" aria-label="Foto: Team bei einer Besprechung am Laptop" style="left:300px;top:42px;width:190px;height:190px"></div>
  <h1 class="abs" style="left:36px;top:118px;font-size:16px;font-weight:800">Lantrava Industrial Suite</h1>
  <p class="abs" style="left:36px;top:142px;font-size:6px;color:var(--grey)">Wir machen Sie zum Dirigenten Ihrer Daten!</p>
  <div class="pill" style="left:36px;top:158px;width:56px;height:12px;background:var(--lime);color:#fff">Sep. 2023</div>
  <div class="brand" style="left:24px;bottom:20px;font-size:13px;color:var(--blue)"><i></i>quamvel</div>
</section>

<!-- 2 agenda -->
<section class="slide" style="left:615px;top:654px">
  <div class="abs" style="left:-300px;top:-70px;width:430px;height:430px;border-radius:50%;background:linear-gradient(160deg,var(--sky),var(--blue))"></div>
  <div class="brand light" style="top:16px;left:16px"><i></i>Lantrava</div>
  <div class="abs" style="left:51px;top:158px;width:84px;height:84px;border-radius:50%;background:var(--lime);color:#fff;font-size:12px;font-weight:700;display:flex;align-items:center;justify-content:center">Agenda</div>
  <div class="agenda-row" style="top:58px">Title text here<span class="line"></span>01</div>
  <div class="agenda-row" style="top:81px">Lorem ipsum dolor sit amet<span class="line"></span>02</div>
  <div class="agenda-row" style="top:105px">Title text here<span class="line"></span>03</div>
  <div class="agenda-row" style="top:128px">Lorem ipsum dolor sit amet<span class="line"></span>04</div>
  <div class="agenda-row" style="top:152px">Title text here<span class="line"></span>05</div>
  <div class="agenda-row" style="top:175px">Lorem ipsum dolor sit amet<span class="line"></span>06</div>
  <div class="agenda-row" style="top:199px">Title text here<span class="line"></span>07</div>
  <div class="agenda-row" style="top:222px">Lorem ipsum dolor sit amet<span class="line"></span>08</div>
  <div class="foot">© 2023 All Rights Reserved by quamvel GmbH</div><div class="pg"></div>
</section>

<!-- 3 divider -->
<section class="slide" style="left:64px;top:976px">
  <div class="brand" style="top:16px;left:16px"><i></i>Lantrava</div>
  <div class="abs" style="left:0;top:66px;width:520px;height:160px;background:linear-gradient(120deg,var(--blue-mid),var(--blue))"></div>
  <div class="abs" style="left:104px;top:112px;font-size:34px;font-weight:300;color:transparent;-webkit-text-stroke:1px rgba(255,255,255,.55)">01</div>
  <div class="abs" style="left:176px;top:106px;color:#fff;font-size:13px;font-weight:700;line-height:1.15">Kapiteltrenner auch<br>zweizeilig möglich</div>
  <div class="abs" style="left:176px;top:142px;color:#fff;font-size:7px">Subheadline</div>
  <div class="abs" style="left:176px;top:153px;width:230px;border-top:1px solid rgba(255,255,255,.4)"></div>
  <div class="pill" style="left:176px;top:168px;width:44px;height:11px;border:1px solid var(--lime);color:var(--lime)">Read more</div>
  <div class="foot">© 2023 All Rights Reserved by quamvel GmbH</div><div class="pg"></div>
</section>

<!-- 4 sub-chapter -->
<section class="slide" style="left:615px;top:976px">
  <div class="abs" style="left:0;top:0;width:520px;height:114px;background:linear-gradient(120deg,var(--blue),var(--blue-mid))"></div>
  <div class="brand light" style="top:16px;left:16px"><i></i>Lantrava</div>
  <div class="abs" style="left:48px;top:68px;color:#fff;font-size:13px;font-weight:700">Unterkapitel</div>
  <div class="abs" style="left:48px;top:87px;color:var(--lime);font-size:7px">Subheadline</div>
  <div class="subitem" style="left:52px;top:138px">Unterkapitelpunkt 01<small>Beschreibung</small></div>
  <div class="subitem" style="left:52px;top:161px">Unterkapitelpunkt 02<small>Beschreibung</small></div>
  <div class="subitem" style="left:52px;top:184px">Unterkapitelpunkt 03<small>Beschreibung</small></div>
  <div class="subitem" style="left:52px;top:207px">Unterkapitelpunkt 04<small>Beschreibung</small></div>
  <div class="subitem" style="left:52px;top:230px">Unterkapitelpunkt 05<small>Beschreibung</small></div>
  <div class="subitem" style="left:273px;top:138px">Unterkapitelpunkt 01<small>Beschreibung</small></div>
  <div class="subitem" style="left:273px;top:161px">Unterkapitelpunkt 02<small>Beschreibung</small></div>
  <div class="subitem" style="left:273px;top:184px">Unterkapitelpunkt 03<small>Beschreibung</small></div>
  <div class="subitem" style="left:273px;top:207px">Unterkapitelpunkt 04<small>Beschreibung</small></div>
  <div class="subitem" style="left:273px;top:230px">Unterkapitelpunkt 05<small>Beschreibung</small></div>
  <div class="foot">© 2023 All Rights Reserved by quamvel GmbH</div><div class="pg"></div>
</section>

<!-- 5 text one column -->
<section class="slide" style="left:64px;top:1297px">
  <div class="hd"><span class="bar"></span><h2>HEADLINE</h2><p>Subheadline</p></div>
  <div class="brand r"><i></i>Lantrava</div>
  <div class="abs" style="left:24px;top:68px;width:460px">
    <p class="lead">Lorem ipsum dolor sit amet, consetetur sadipscing elitr, sed diam nonumy eirmod tempor invidunt ut labore et dolore magna.</p>
    <ul class="body" style="list-style:none;margin-top:3px">At vero eos et accusam et justo duo dolores et ea rebum. Stet clita kasd, no sea takimata sanctus est Lorem ipsum dolor sit.
      <li>Lorem ipsum dolor sit amet, consetetur sadipscing elitr, sed diam nonumy eirmod tempor invidunt ut labore et dolore.
        <ul><li>At vero eos et accusam et justo duo dolores et ea rebum<ul><li>At vero eos et accusam et justo duo dolores et ea rebum</li></ul></li></ul>
      </li>
    </ul>
  </div>
  <div class="foot">© 2023 All Rights Reserved by quamvel GmbH</div><div class="pg"></div>
</section>

<!-- 6 text two columns -->
<section class="slide" style="left:615px;top:1297px">
  <div class="hd"><span class="bar"></span><h2>HEADLINE</h2><p>Subheadline</p></div>
  <div class="brand r"><i></i>Lantrava</div>
  <div class="abs" style="left:24px;top:68px;width:220px">
    <p class="lead">Lorem ipsum dolor sit amet, consetetur sadipscing elitr, sed diam nonumy eirmod tempor invidunt ut labore et dolore magna.</p>
    <ul class="body" style="list-style:none;margin-top:3px">At vero eos et accusam et justo duo dolores et ea rebum. Stet clita kasd, no sea takimata sanctus est Lorem ipsum dolor sit.
      <li>Lorem ipsum dolor sit amet, consetetur sadipscing elitr, sed diam nonumy eirmod tempor invidunt ut labore et dolore<ul><li>At vero eos et accusam et justo duo dolores et ea rebum</li><li>At vero eos et accusam et justo duo dolores et ea rebum</li></ul></li>
    </ul>
  </div>
  <div class="abs" style="left:276px;top:68px;width:220px">
    <p class="lead">Lorem ipsum dolor sit amet, consetetur sadipscing elitr, sed diam nonumy eirmod tempor invidunt ut labore et dolore magna.</p>
    <ul class="body" style="list-style:none;margin-top:3px">At vero eos et accusam et justo duo dolores et ea rebum. Stet clita kasd, no sea takimata sanctus est Lorem ipsum dolor sit.
      <li>Lorem ipsum dolor sit amet, consetetur sadipscing elitr, sed diam nonumy eirmod tempor invidunt ut labore et dolore<ul><li>At vero eos et accusam et justo duo dolores et ea rebum</li><li>At vero eos et accusam et justo duo dolores et ea rebum</li></ul></li>
    </ul>
  </div>
  <div class="foot">© 2023 All Rights Reserved by quamvel GmbH</div><div class="pg"></div>
</section>

<!-- 7 image + text -->
<section class="slide" style="left:64px;top:1619px">
  <div class="hd"><span class="bar"></span><h2>HEADLINE</h2><p>Subheadline</p></div>
  <div class="brand r"><i></i>Lantrava</div>
  <div class="ring" style="left:32px;top:78px;width:170px;height:170px"></div>
  <div class="photo" role="img" aria-label="Foto: Laptop mit Produktionsdaten in einer Fabrikhalle" style="left:48px;top:78px;width:158px;height:158px;background:radial-gradient(circle at 40% 40%,#9fb2c2,#34506b 75%)"></div>
  <div class="abs" style="left:248px;top:70px;width:246px">
    <p class="lead" style="margin-bottom:6px">Lorem ipsum dolor sit amet, consetetur sadipscing sed diam nonumy</p>
    <div class="body">At vero eos et accusam et justo duo dolores et ea rebum. Stet clita kasd, no sea takimata sanctus est Lorem ipsum dolor sit. Lorem ipsum dolor sit amet, consetetur sadipscing elitr, sed diam nonumy eirmod tempor invidunt ut labore et dolore</div>
    <ul class="body" style="margin-top:6px">
      <li>Lorem ipsum dolor sit amet, consetetur sadipscing elitr, sed diam nonumy eirmod tempor invidunt ut labore et dolore<ul style="list-style:none"><li>At vero eos et accusam et justo duo dolores et ea rebum</li><li>At vero eos et accusam et justo duo dolores et ea rebum</li></ul></li>
      <li style="margin-top:6px">Lorem ipsum dolor sit amet, consetetur sadipscing elitr, sed diam nonumy eirmod tempor invidunt ut labore et dolore<ul style="list-style:none"><li>At vero eos et accusam et justo duo dolores et ea rebum</li><li>At vero eos et accusam et justo duo dolores et ea rebum</li></ul></li>
    </ul>
  </div>
  <div class="foot">© 2023 All Rights Reserved by quamvel GmbH</div><div class="pg"></div>
</section>

<!-- 8 headline only -->
<section class="slide" style="left:615px;top:1619px">
  <div class="hd"><span class="bar"></span><h2>HEADLINE</h2><p>Subheadline</p></div>
  <div class="brand r"><i></i>Lantrava</div>
  <div class="foot">© 2023 All Rights Reserved by quamvel GmbH</div><div class="pg"></div>
</section>

<!-- 9 three cards -->
<section class="slide" style="left:64px;top:1941px">
  <div class="hd"><span class="bar"></span><h2>HEADLINE</h2><p>Subheadline</p></div>
  <div class="brand r"><i></i>Lantrava</div>
  <div class="card" style="left:40px"><div class="ic"></div><h3>CHALLENGE</h3>
    <div class="body">Lorem ipsum dolor sit amet, consetetur lacus sadipscing elitr, sed diam nonumy eirmod tempor invidunt ut nam labore et dolore magna.<ul><li>Dritte Ebene. Lorem ipsum<ul><li>Vierte Ebene. Lorem ipsum<ul style="list-style:none"><li>Fünfte Ebene. Lorem ipsum</li></ul></li></ul></li></ul></div></div>
  <div class="card" style="left:190px"><div class="ic"></div><h3>SOLUTION</h3>
    <div class="body">Lorem ipsum dolor sit amet, consetetur lacus sadipscing elitr, sed diam nonumy eirmod tempor invidunt ut nam labore et dolore magna.<ul><li>Dritte Ebene. Lorem ipsum<ul><li>Vierte Ebene. Lorem ipsum<ul style="list-style:none"><li>Fünfte Ebene. Lorem ipsum</li></ul></li></ul></li></ul></div></div>
  <div class="card" style="left:340px"><div class="ic"></div><h3>BENEFIT</h3>
    <div class="body">Lorem ipsum dolor sit amet, consetetur lacus sadipscing elitr, sed diam nonumy eirmod tempor invidunt ut nam labore et dolore magna.<ul><li>Dritte Ebene. Lorem ipsum<ul><li>Vierte Ebene. Lorem ipsum<ul style="list-style:none"><li>Fünfte Ebene. Lorem ipsum</li></ul></li></ul></li></ul></div></div>
  <div class="foot">© 2023 All Rights Reserved by quamvel GmbH</div><div class="pg"></div>
</section>

<!-- 10 IT/OT infographic placeholder -->
<section class="slide" style="left:615px;top:1941px">
  <div class="hd"><span class="bar"></span><h2>HEADLINE</h2><p>Subheadline</p></div>
  <div class="brand r"><i></i>Lantrava</div>
  <div class="abs" role="img" aria-label="Infografik: Verbindung von IT-Systemen und OT-Produktionsanlagen über den Integrationsbus" style="left:0;top:62px;width:520px;height:200px;background:linear-gradient(180deg,var(--blue-deep) 0%,var(--blue) 53%,#e6f1f9 53%,#d7e8f4 100%)"></div>
  <div class="foot">© 2023 All Rights Reserved by quamvel GmbH</div><div class="pg"></div>
</section>

<!-- 11 break -->
<section class="slide" style="left:64px;top:2262px;background:linear-gradient(160deg,var(--blue-mid),var(--blue-deep))">
  <div class="abs" style="left:116px;top:44px;font-family:Nunito,sans-serif;font-weight:900;font-size:52px;color:#fff;line-height:1">Break</div>
  <div class="abs" style="left:276px;top:46px;width:140px;height:64px;background:var(--lime);border-radius:4px"></div>
  <svg class="abs" style="left:282px;top:108px" width="16" height="12"><path d="M0 0 H16 L2 12Z" fill="#b9d84a"/></svg>
  <div class="abs" style="left:282px;top:48px;font-family:Nunito,sans-serif;font-weight:900;font-size:52px;color:var(--blue-mid);line-height:1.1">Time</div>
  <div class="abs" style="left:118px;top:116px;color:#fff;font-size:8px">Let's take a 30-minute break</div>
  <div class="abs" style="left:92px;top:158px;width:350px;height:96px;background:#fff;border-radius:4px;box-shadow:0 3px 8px rgba(0,0,0,.2)">
    <div class="abs" style="left:174px;top:12px;height:72px;border-left:1px solid #dfe6ec"></div>
    <ul class="abs" style="left:24px;top:22px;font-size:7px;font-weight:700;line-height:2.9;color:var(--ink);list-style:none">
      <li><span style="color:var(--lime)">•</span>&nbsp; Title text here</li>
      <li><span style="color:var(--lime)">•</span>&nbsp; Title text here</li>
      <li><span style="color:var(--lime)">•</span>&nbsp; Title text here</li>
    </ul>
    <div class="abs" style="left:174px;width:176px;top:20px;text-align:center;font-family:Nunito,sans-serif;font-size:32px;font-weight:900;color:var(--blue-mid)">09.35</div>
    <div class="abs" style="left:174px;width:176px;top:64px;text-align:center;font-size:8px;color:var(--lime)">Next Discussion</div>
  </div>
</section>

<!-- 12 team -->
<section class="slide" style="left:615px;top:2262px">
  <div class="hd"><h2>MEET THE TEAM</h2><p>Subtitle text goes here</p></div>
  <div class="brand r"><i></i>Lantrava</div>
  <div class="member" style="left:46px"><div class="ph" role="img" aria-label="Platzhalter Teamfoto"></div><h4>MAX MUSTER</h4><p>Kurze Beschreibung zur Person und ihrer Rolle</p><div class="soc"><i></i><i></i><i></i><i></i></div></div>
  <div class="member" style="left:153px"><div class="ph" role="img" aria-label="Platzhalter Teamfoto"></div><h4>MAX MUSTER</h4><p>Kurze Beschreibung zur Person und ihrer Rolle</p><div class="soc"><i></i><i></i><i></i><i></i></div></div>
  <div class="member" style="left:260px"><div class="ph" role="img" aria-label="Platzhalter Teamfoto"></div><h4>MAX MUSTER</h4><p>Kurze Beschreibung zur Person und ihrer Rolle</p><div class="soc"><i></i><i></i><i></i><i></i></div></div>
  <div class="member" style="left:367px"><div class="ph" role="img" aria-label="Platzhalter Teamfoto"></div><h4>MAX MUSTER</h4><p>Kurze Beschreibung zur Person und ihrer Rolle</p><div class="soc"><i></i><i></i><i></i><i></i></div></div>
  <div class="foot">© 2023 All Rights Reserved by quamvel GmbH</div><div class="pg"></div>
</section>

<!-- 13 number table -->
<section class="slide" style="left:64px;top:2585px">
  <div class="hd"><span class="bar"></span><h2>TABELLEN</h2><p>Subheadline</p></div>
  <div class="brand r"><i></i>Lantrava</div>
  <div class="abs" style="left:24px;top:74px;width:472px">
    <table class="num">
      <tr><th style="background:none"></th><th>July</th><th>August</th><th>September</th><th>Q3 2022</th></tr>
      <tr class="hl"><td colspan="5" style="background:#cfe6f5"></td></tr>
      <tr><td>CSS Contract</td><td>$ 409.277,55</td><td>$ 363.630,05</td><td>$ 383.461,63</td><td>$ 1.156.319,23</td></tr>
      <tr><td>CSS Perm</td><td>$ -</td><td>$ 17.200,00</td><td>$ -</td><td>$ 17.200,00</td></tr>
      <tr><td>Avg Weekly</td><td>$ 81.845,51</td><td>$ 90.207,51</td><td>$ 89.365,41</td><td></td></tr>
      <tr><td>CSS Total Rev</td><td>$ 409.277,55</td><td>$ 380.830,05</td><td>$ 383.461,63</td><td><b>$ 1.173.519,23</b></td></tr>
      <tr class="hl"><td colspan="5"></td></tr>
      <tr><td>CSS Perm</td><td>$ -</td><td>$ 17.200,00</td><td>$ -</td><td>$ 17.200,00</td></tr>
      <tr><td>Avg Weekly</td><td>$ 18.348,68</td><td>$ 23.467,18</td><td>$ 19.858,91</td><td></td></tr>
      <tr><td>CSS Total GP</td><td>$ 91.742,89</td><td>$ 93.828,71</td><td>$ 79.435,63</td><td><b>$ 265.007,23</b></td></tr>
      <tr><td>Gross Margin %</td><td>22,4%</td><td>26,0%</td><td>22,5%</td><td><b>23,6%</b></td></tr>
    </table>
  </div>
  <div class="foot">© 2023 All Rights Reserved by quamvel GmbH</div><div class="pg"></div>
</section>

<!-- 14 text table -->
<section class="slide" style="left:615px;top:2585px">
  <div class="hd"><span class="bar"></span><h2>TABELLEN</h2><p>Subheadline</p></div>
  <div class="brand r"><i></i>Lantrava</div>
  <div class="abs" style="left:24px;top:68px;width:472px">
    <table class="txt">
      <tr><th style="background:none"></th><th style="background:var(--blue)">TITLE</th><th style="background:var(--sky)">TITLE</th><th style="background:var(--lime)">TITLE</th><th style="background:#a3abb4">TITLE</th></tr>
      <tr><td>Description Here</td><td>there are many variations of passages of lorem ipsum available, but the majority have suffered alteration in some form, by injected.</td><td>there are many variations of passages of lorem ipsum available, but the majority have suffered alteration in some form, by injected.</td><td>there are many variations of passages of lorem ipsum available, but the majority have suffered alteration in some form, by injected.</td><td>there are many variations of passages of lorem ipsum available, but the majority have suffered alteration in some form, by injected.</td></tr>
      <tr><td>Description Here</td><td>there are many variations of passages of lorem ipsum available, but the majority have suffered alteration in some form, by injected.</td><td>there are many variations of passages of lorem ipsum available, but the majority have suffered alteration in some form, by injected.</td><td>there are many variations of passages of lorem ipsum available, but the majority have suffered alteration in some form, by injected.</td><td>there are many variations of passages of lorem ipsum available, but the majority have suffered alteration in some form, by injected.</td></tr>
      <tr><td>Description Here</td><td>there are many variations of passages of lorem ipsum available, but the majority have suffered alteration in some form, by injected.</td><td>there are many variations of passages of lorem ipsum available, but the majority have suffered alteration in some form, by injected.</td><td>there are many variations of passages of lorem ipsum available, but the majority have suffered alteration in some form, by injected.</td><td>there are many variations of passages of lorem ipsum available, but the majority have suffered alteration in some form, by injected.</td></tr>
    </table>
  </div>
  <div class="foot">© 2023 All Rights Reserved by quamvel GmbH</div><div class="pg"></div>
</section>

<!-- 15 chart analysis -->
<section class="slide" style="left:64px;top:2905px">
  <div class="hd"><span class="bar"></span><h2>CHART ANALYSIS</h2><p>Subheadline</p></div>
  <div class="brand r"><i></i>Lantrava</div>
  <svg class="abs" style="left:24px;top:72px" width="472" height="200" viewBox="0 0 472 200" font-family="Open Sans,sans-serif">
    <rect x="0" y="0" width="118" height="36" fill="#1ea3e2"/><rect x="118" y="0" width="118" height="36" fill="#b9d84a"/>
    <rect x="236" y="0" width="118" height="36" fill="#7d8895"/><rect x="354" y="0" width="118" height="36" fill="#0d3f78"/>
    <g fill="#fff" font-size="6.5" font-weight="700" text-anchor="middle">
      <circle cx="59" cy="12" r="5"/><text x="59" y="29">Insert title here</text>
      <circle cx="177" cy="12" r="5"/><text x="177" y="29">Insert title here</text>
      <circle cx="295" cy="12" r="5"/><text x="295" y="29">Insert title here</text>
      <circle cx="413" cy="12" r="5"/><text x="413" y="29">Insert title here</text>
    </g>
    <g stroke="#e3e8ed"><path d="M14 50 H472 M14 74 H472 M14 98 H472 M14 122 H472 M14 146 H472 M14 170 H472"/></g>
    <g font-size="4.5" fill="#7d8895"><text x="0" y="52">90</text><text x="0" y="100">50</text><text x="0" y="172">0</text>
      <text x="64" y="182">2015</text><text x="176" y="182">2016</text><text x="290" y="182">2017</text><text x="404" y="182">2018</text></g>
    <g>
      <rect x="40" y="152" width="14" height="18" fill="#1ea3e2"/><rect x="54" y="108" width="14" height="62" fill="#b9d84a"/><rect x="68" y="140" width="14" height="30" fill="#a9b2bc"/><rect x="82" y="124" width="14" height="46" fill="#0d3f78"/>
      <rect x="150" y="148" width="14" height="22" fill="#1ea3e2"/><rect x="164" y="140" width="14" height="30" fill="#b9d84a"/><rect x="178" y="138" width="14" height="32" fill="#a9b2bc"/><rect x="192" y="84" width="14" height="86" fill="#0d3f78"/>
      <rect x="262" y="136" width="14" height="34" fill="#1ea3e2"/><rect x="276" y="120" width="14" height="50" fill="#b9d84a"/><rect x="290" y="136" width="14" height="34" fill="#a9b2bc"/><rect x="304" y="110" width="14" height="60" fill="#0d3f78"/>
      <rect x="376" y="126" width="14" height="44" fill="#1ea3e2"/><rect x="390" y="138" width="14" height="32" fill="#b9d84a"/><rect x="404" y="138" width="14" height="32" fill="#a9b2bc"/><rect x="418" y="114" width="14" height="56" fill="#0d3f78"/>
    </g>
  </svg>
  <div class="foot">© 2023 All Rights Reserved by quamvel GmbH</div><div class="pg"></div>
</section>

<!-- 16 chart infographic -->
<section class="slide" style="left:615px;top:2905px">
  <div class="hd"><span class="bar"></span><h2>CHART INFOGRAPHIC</h2><p>Subheadline</p></div>
  <div class="brand r"><i></i>Lantrava</div>
  <svg class="abs" style="left:24px;top:70px" width="472" height="200" viewBox="0 0 472 200" font-family="Open Sans,sans-serif">
    <g font-size="5" font-weight="700" text-anchor="middle" fill="#1d2b3a"><text x="65" y="8">YOUR TITLE HERE</text><text x="200" y="8">YOUR TITLE HERE</text><text x="370" y="8">YOUR TITLE HERE</text></g>
    <rect x="10" y="16" width="114" height="116" fill="#fff"/><rect x="146" y="16" width="110" height="116" fill="#fff"/><rect x="278" y="16" width="184" height="116" fill="#fff"/>
    <g><rect x="40" y="36" width="58" height="9" fill="#1ea3e2"/><rect x="40" y="54" width="28" height="9" fill="#b9d84a"/><rect x="40" y="72" width="38" height="9" fill="#1ea3e2"/><rect x="40" y="90" width="48" height="9" fill="#b9d84a"/><rect x="40" y="108" width="26" height="9" fill="#1ea3e2"/></g>
    <g transform="translate(200 68)" fill="none" stroke-width="14">
      <circle r="26" stroke="#0d3f78"/>
      <circle r="26" stroke="#1ea3e2" stroke-dasharray="50 114" transform="rotate(-90)"/>
      <circle r="26" stroke="#b9d84a" stroke-dasharray="30 134" stroke-dashoffset="-50" transform="rotate(-90)"/>
    </g>
    <path d="M292 110 L310 60 L340 90 L370 55 L400 82 L430 50 L450 70 V118 H292Z" fill="#1ea3e2"/>
    <path d="M292 118 L310 90 L340 70 L370 96 L400 76 L430 92 L450 84 V118Z" fill="#b9d84a"/>
    <g font-size="4.5" fill="#7d8895" text-anchor="middle">
      <text x="67" y="150">There are many variations of</text><text x="67" y="156">passages of lorem ipsum available.</text>
      <text x="200" y="150">There are many variations of</text><text x="200" y="156">passages of lorem ipsum available.</text>
      <text x="370" y="150">There are many variations of</text><text x="370" y="156">passages of lorem ipsum available.</text>
    </g>
  </svg>
  <div class="foot">© 2023 All Rights Reserved by quamvel GmbH</div><div class="pg"></div>
</section>

<!-- 17 world maps -->
<section class="slide" style="left:64px;top:3228px">
  <div class="hd"><span class="bar"></span><h2>HEADLINE</h2><p>Subheadline</p></div>
  <div class="brand r"><i></i>Lantrava</div>
  <div class="abs" role="img" aria-label="Weltkarte in Grautönen" style="left:140px;top:34px;width:352px;height:170px;background:radial-gradient(ellipse at 50% 45%,#b9c0c8,#d6dbe0 70%,transparent 72%)"></div>
  <div class="abs" style="left:28px;top:188px;font-size:15px;font-weight:700">World Maps</div>
  <div class="abs body" style="left:28px;top:212px;width:130px">Lorem ipsum dolor sit amet, consetetur et nam adipiscing elit. Morbi eget dolor sit amet nulla imperdiet congue. Integer placerat eros enim.</div>
  <div class="stat" style="left:186px;background:var(--blue-deep)"><svg width="22" height="22"><circle cx="11" cy="11" r="8" fill="none" stroke="#fff" stroke-width="4" stroke-dasharray="40 50"/></svg><div><b>80%</b><small>Lorem ipsum dolor sit</small></div></div>
  <div class="stat" style="left:288px;background:var(--sky)"><svg width="22" height="22"><circle cx="11" cy="11" r="8" fill="none" stroke="#fff" stroke-width="4" stroke-dasharray="43 50"/></svg><div><b>85%</b><small>Lorem ipsum dolor sit</small></div></div>
  <div class="stat" style="left:390px;background:var(--lime)"><svg width="22" height="22"><circle cx="11" cy="11" r="8" fill="none" stroke="#fff" stroke-width="4" stroke-dasharray="38 50"/></svg><div><b>75%</b><small>Lorem ipsum dolor sit</small></div></div>
  <div class="foot">© 2023 All Rights Reserved by quamvel GmbH</div><div class="pg"></div>
</section>

<!-- 18 thank you -->
<section class="slide" style="left:615px;top:3228px;background:linear-gradient(150deg,var(--blue),var(--blue-deep))">
  <div class="abs" style="left:328px;top:40px;width:240px;height:240px;border-radius:50%;background:var(--sky)"></div>
  <div class="abs" style="left:300px;top:132px;width:80px;height:80px;border-radius:50%;background:var(--lime);display:flex;align-items:center;justify-content:center"><div class="brand light" style="position:static;font-size:7px"><i></i>Lantrava</div></div>
  <div class="abs" style="left:372px;top:98px;color:#fff;font-size:18px;font-weight:700;text-align:center;width:130px">Vielen Dank</div>
  <div class="abs" style="left:362px;top:120px;color:#fff;font-size:8px;font-weight:600;text-align:center;width:150px">für Ihre Aufmerksamkeit!</div>
  <div class="abs" style="left:36px;top:74px;color:#fff;font-size:12px;font-weight:700">Vorname, Name</div>
  <div class="abs" style="left:36px;top:108px;color:#fff;font-size:7px">Abteilung | Position</div>
  <div class="abs" style="left:36px;top:128px;width:148px;border-top:1px solid rgba(255,255,255,.35)"></div>
  <div class="abs" style="left:36px;top:140px;color:#fff;font-size:5.5px;line-height:2.6">
    <div>☎&nbsp; +1 (000) 123 456 789</div>
    <div>✉&nbsp; vorname.name@quamvel.de</div>
    <div style="line-height:1.3">⌖&nbsp; quamvel GmbH | Lindenweg 12 | 80331 Musterstadt |<br>&nbsp;&nbsp;&nbsp;Deutschland</div>
  </div>
  <div class="brand light" style="left:36px;bottom:26px;font-size:15px"><i></i>quamvel</div>
</section>

</body>
</html>
```